Financial Services Company power point theme design

We need a PowerPoint theme designed for client presentations and company orientations. We do like modern designs using blue colors. attached is our logos the logo colors may change as needed to fit the theme. Landscape 16: 9 is acceptable

Industry/Entity Type

Financial Service

Colors

Designer to choose colors to be used in the design.

```html
<!DOCTYPE html>
<html lang="en">
<head>
<meta charset="utf-8">
<title>Keystone Ridge Financial – Presentation Theme</title>
<link href="https://fonts.googleapis.com/css2?family=Mulish:wght@300;400;600;700&display=swap" rel="stylesheet">
<style>
:root{
  --bg:#f1f1f3;
  --blue:#45ade0;
  --blue-soft:#7cc4ea;
  --navy:#1f3b6f;
  --steel:#7aa3cb;
  --steel-dark:#3e7db4;
  --ink:#5c6470;
  --line:#d5dbe2;
  --panel:#eceff2;
}
*{box-sizing:border-box;margin:0;padding:0}
html,body{width:1200px;height:1200px;overflow:hidden;background:var(--bg)}
body{font-family:"Mulish",sans-serif;color:var(--ink)}
.canvas{position:relative;width:1200px;height:1200px;background:var(--bg)}
.slide{position:absolute;width:228px;height:158px;background:#fff;overflow:hidden;box-shadow:0 0 0 1px #e2e4e8}
.c1{left:98px}.c2{left:357px}.c3{left:615px}.c4{left:874px}
.r1{top:50px}.r2{top:238px}.r3{top:426px}.r4{top:615px}.r5{top:803px}.r6{top:991px}
.abs{position:absolute}
.fill{position:absolute;inset:0}
.title{position:absolute;left:10px;top:16px;font-size:9.6px;font-weight:400;color:var(--blue);white-space:nowrap}
.tiny{font-size:3px;line-height:1.4;color:var(--ink)}
.tiny.white{color:#fff}
.brand{position:absolute;font-size:3.4px;font-weight:700;color:var(--navy);letter-spacing:.25px;text-transform:uppercase;white-space:nowrap;display:flex;align-items:center;gap:2px}
.brand::before{content:"";width:5px;height:5px;background:var(--navy);display:block}
.brand.white{color:#fff}.brand.white::before{background:#fff}
.foot{left:10px;bottom:5px}
.pg{position:absolute;right:8px;bottom:5px;font-size:3px;color:#999}
.photo-desk{background:linear-gradient(135deg,#e9eef3 0%,#f8fafb 55%,#dfe7ee 100%)}
.photo-blue{background:linear-gradient(135deg,#3f9fd3 0%,#5db9e4 55%,#86cdee 100%)}
.list{list-style:none}
.list li{font-size:3px;line-height:1.5;color:var(--ink);padding-left:3px;position:relative}
.list li::before{content:"•";position:absolute;left:0;color:var(--navy)}
.hdr{position:absolute;height:5px;background:var(--blue);color:#fff;font-size:2.8px;font-weight:700;padding-left:2px;line-height:5px}
</style>
</head>
<body>
<svg width="0" height="0" style="position:absolute" aria-hidden="true">
  <defs>
    <symbol id="col-chart" viewBox="0 0 100 44">
      <line x1="6" y1="2" x2="6" y2="34" stroke="#ccc" stroke-width=".4"/>
      <line x1="6" y1="34" x2="98" y2="34" stroke="#ccc" stroke-width=".4"/>
      <g>
        <rect x="12" y="16" width="4" height="18" fill="#1f3b6f"/><rect x="16.5" y="24" width="4" height="10" fill="#45ade0"/><rect x="21" y="28" width="4" height="6" fill="#c9d3dc"/>
        <rect x="34" y="20" width="4" height="14" fill="#1f3b6f"/><rect x="38.5" y="12" width="4" height="22" fill="#45ade0"/><rect x="43" y="28" width="4" height="6" fill="#c9d3dc"/>
        <rect x="56" y="18" width="4" height="16" fill="#1f3b6f"/><rect x="60.5" y="26" width="4" height="8" fill="#45ade0"/><rect x="65" y="22" width="4" height="12" fill="#c9d3dc"/>
        <rect x="78" y="8" width="4" height="26" fill="#1f3b6f"/><rect x="82.5" y="20" width="4" height="14" fill="#45ade0"/><rect x="87" y="16" width="4" height="18" fill="#c9d3dc"/>
      </g>
      <g font-size="2.6" fill="#888" font-family="Mulish,sans-serif">
        <text x="12" y="38">Category 1</text><text x="34" y="38">Category 2</text><text x="56" y="38">Category 3</text><text x="78" y="38">Category 4</text>
        <text x="30" y="43">■ Series 1  ■ Series 2  ■ Series 3</text>
      </g>
    </symbol>
    <symbol id="line-chart" viewBox="0 0 100 44">
      <line x1="6" y1="2" x2="6" y2="34" stroke="#ccc" stroke-width=".4"/>
      <line x1="6" y1="34" x2="98" y2="34" stroke="#ccc" stroke-width=".4"/>
      <polyline points="10,22 38,14 66,26 94,10" fill="none" stroke="#1f3b6f" stroke-width=".8"/>
      <polyline points="10,12 38,26 66,18 94,20" fill="none" stroke="#45ade0" stroke-width=".8"/>
      <polyline points="10,28 38,22 66,12 94,26" fill="none" stroke="#a9c3da" stroke-width=".8"/>
      <g font-size="2.6" fill="#888" font-family="Mulish,sans-serif">
        <text x="10" y="38">Category 1</text><text x="36" y="38">Category 2</text><text x="62" y="38">Category 3</text><text x="86" y="38">Category 4</text>
        <text x="30" y="43">— Series 1  — Series 2  — Series 3</text>
      </g>
    </symbol>
    <symbol id="hb0" viewBox="0 0 10 10"><circle cx="5" cy="5" r="4" fill="#fff" stroke="#1f3b6f" stroke-width=".6"/></symbol>
    <symbol id="hb1" viewBox="0 0 10 10"><circle cx="5" cy="5" r="4" fill="#fff" stroke="#1f3b6f" stroke-width=".6"/><path d="M5 5L5 1A4 4 0 0 1 9 5Z" fill="#1f3b6f"/></symbol>
    <symbol id="hb2" viewBox="0 0 10 10"><circle cx="5" cy="5" r="4" fill="#fff" stroke="#1f3b6f" stroke-width=".6"/><path d="M5 1A4 4 0 0 1 5 9Z" fill="#1f3b6f"/></symbol>
    <symbol id="hb3" viewBox="0 0 10 10"><circle cx="5" cy="5" r="4" fill="#fff" stroke="#1f3b6f" stroke-width=".6"/><path d="M5 5L5 1A4 4 0 1 1 1 5Z" fill="#1f3b6f"/></symbol>
    <symbol id="hb4" viewBox="0 0 10 10"><circle cx="5" cy="5" r="4" fill="#1f3b6f"/></symbol>
    <symbol id="tick" viewBox="0 0 10 10"><path d="M2 5.5L4.2 7.6L8 2.6" fill="none" stroke="#1f3b6f" stroke-width="1.3"/></symbol>
    <symbol id="cross" viewBox="0 0 10 10"><path d="M3 3L7 7M7 3L3 7" stroke="#1f3b6f" stroke-width="1.2"/></symbol>
  </defs>
</svg>

<main class="canvas">

  <!-- 1 Title slide -->
  <section class="slide c1 r1">
    <div class="fill photo-desk" role="img" aria-label="Soft photo of a desk with keyboard and paperwork"></div>
    <svg class="fill" viewBox="0 0 228 158" width="228" height="158">
      <polygon points="2,52 45,34 88,52 45,70" fill="#45ade0" opacity=".85"/>
      <polygon points="120,52 172,32 224,52 172,72" fill="#45ade0" opacity=".85"/>
      <polygon points="48,92 116,64 184,92 116,120" fill="#45ade0" opacity=".9"/>
    </svg>
    <div class="brand" style="left:88px;top:28px">Keystone Ridge</div>
    <div class="abs" style="left:0;width:228px;top:82px;text-align:center;color:#fff;font-size:9.6px;font-weight:300">Powerpoint Title</div>
    <div class="abs" style="left:0;width:228px;top:95px;text-align:center;color:#fff;font-size:3.2px">July 2018</div>
    <div class="abs tiny" style="left:10px;bottom:5px;font-size:2.6px">Disclaimer: Past performance does not guarantee future results. Please review all terms carefully.</div>
  </section>

  <!-- 2 Title slide, blue -->
  <section class="slide c2 r1">
    <div class="fill photo-blue" role="img" aria-label="Blue toned photo of hands reviewing financial charts"></div>
    <svg class="fill" viewBox="0 0 228 158" width="228" height="158">
      <polygon points="0,0 6,0 74,158 66,158" fill="#fff" opacity=".8"/>
    </svg>
    <div class="abs" style="right:10px;top:26px;color:#fff;font-size:9.6px;font-weight:300">Presentation Title</div>
    <div class="abs" style="right:10px;top:40px;color:#fff;font-size:3px">Date</div>
    <div class="brand white" style="right:10px;top:128px">Keystone Ridge</div>
    <div class="abs tiny white" style="right:10px;bottom:5px;width:86px;text-align:right;font-size:2.5px">Disclaimer: Past performance does not guarantee future results. Review all terms carefully.</div>
  </section>

  <!-- 3 Alternate cover -->
  <section class="slide c3 r1">
    <div class="fill photo-desk" role="img" aria-label="Light photo of a desk with keyboard, pen and charts"></div>
    <svg class="fill" viewBox="0 0 228 158" width="228" height="158">
      <polygon points="70,0 90,0 168,158 146,158" fill="#45ade0" opacity=".85"/>
      <polygon points="96,0 99,0 176,158 173,158" fill="#1f3b6f"/>
    </svg>
    <div class="brand" style="right:12px;top:22px">Keystone Ridge</div>
    <div class="abs tiny" style="right:10px;bottom:5px;width:86px;text-align:right;font-size:2.5px">Disclaimer: Past performance does not guarantee future results. Review all terms carefully.</div>
  </section>

  <!-- 4 Contents -->
  <section class="slide c4 r1">
    <div class="abs photo-blue" style="left:0;top:0;width:60px;height:143px" role="img" aria-label="Blue toned photo of a person writing"></div>
    <div class="title" style="left:68px;top:24px;font-size:9px">Contents</div>
    <div class="abs" style="left:68px;top:46px;width:150px;display:grid;grid-template-columns:74px 74px;row-gap:8px">
      <div class="tiny"><b style="color:var(--blue);font-size:5px">03/</b> Lorem ipsum dolor sit amet dolor</div>
      <div class="tiny"><b style="color:var(--blue);font-size:5px">15/</b> Lorem ipsum dolor sit amet dolor</div>
      <div class="tiny"><b style="color:var(--blue);font-size:5px">06/</b> Lorem ipsum dolor sit amet dolor</div>
      <div class="tiny"><b style="color:var(--blue);font-size:5px">18/</b> Lorem ipsum dolor sit amet dolor</div>
      <div class="tiny"><b style="color:var(--blue);font-size:5px">09/</b> Lorem ipsum dolor sit amet dolor</div>
      <div class="tiny"><b style="color:var(--blue);font-size:5px">21/</b> Lorem ipsum dolor sit amet dolor</div>
      <div class="tiny"><b style="color:var(--blue);font-size:5px">12/</b> Lorem ipsum dolor sit amet dolor</div>
    </div>
    <div class="brand foot">Keystone Ridge</div><div class="pg">4</div>
  </section>

  <!-- 5 Section divider -->
  <section class="slide c1 r2">
    <div class="abs photo-blue" style="left:0;top:0;width:228px;height:143px" role="img" aria-label="Blue toned photo of a business meeting"></div>
    <div class="abs" style="left:17px;top:30px;color:#fff;font-size:15px;font-weight:300;line-height:1.1">Lorem ipsum<br>dolor sit amet</div>
    <div class="abs" style="left:17px;top:68px;color:#fff;font-size:5px;font-weight:300">Lorem ipsum dolor sit amet</div>
    <div class="brand foot">Keystone Ridge</div><div class="pg">5</div>
  </section>

  <!-- 6 About us -->
  <section class="slide c2 r2">
    <div class="abs photo-blue" style="left:0;top:0;width:60px;height:143px;background:linear-gradient(160deg,#2f8fc4,#6fc0e8)" role="img" aria-label="Blue toned photo of an office building"></div>
    <div class="title" style="left:68px;top:24px;font-size:9px">About Us</div>
    <p class="abs tiny" style="left:68px;top:38px;width:70px">Our clients' goals, objectives and dreams come first. We listen, evaluate and help you identify both short and long term goals, helping you make informed decisions about every aspect of your financial life.</p>
    <p class="abs tiny" style="left:142px;top:38px;width:72px">From saving for college to owning a business, our team of experts will guide you through all the moving pieces and reinforce the positive choices you have made, now and throughout your lifetime.</p>
    <div class="abs" style="left:68px;top:88px;display:flex;gap:4px">
      <div style="width:46px;height:50px;border:.6px solid var(--blue);text-align:center;padding-top:4px">
        <svg width="7" height="7" viewBox="0 0 10 10"><circle cx="5" cy="5" r="4" fill="none" stroke="#45ade0" stroke-width="1"/></svg>
        <div style="font-size:3px;font-weight:700;color:var(--blue)">MISSION</div>
        <div class="tiny" style="padding:1px 3px">Our mission is to educate and guide our clients through every stage.</div>
      </div>
      <div style="width:46px;height:50px;border:.6px solid var(--blue);text-align:center;padding-top:4px">
        <svg width="7" height="7" viewBox="0 0 10 10"><rect x="1" y="3" width="8" height="5" fill="none" stroke="#45ade0" stroke-width="1"/></svg>
        <div style="font-size:3px;font-weight:700;color:var(--blue)">VALUE</div>
        <div class="tiny" style="padding:1px 3px">Our value is being your go-to resource for any financial question.</div>
      </div>
      <div style="width:46px;height:50px;border:.6px solid var(--blue);text-align:center;padding-top:4px">
        <svg width="7" height="7" viewBox="0 0 10 10"><path d="M2 8L5 2L8 8Z" fill="none" stroke="#45ade0" stroke-width="1"/></svg>
        <div style="font-size:3px;font-weight:700;color:var(--blue)">EXPERTISE</div>
        <div class="tiny" style="padding:1px 3px">Each advisor brings a unique approach to serving our clients.</div>
      </div>
    </div>
    <div class="brand foot">Keystone Ridge</div><div class="pg">6</div>
  </section>

  <!-- 7 Our team -->
  <section class="slide c3 r2">
    <div class="title">Our Team</div>
    <div class="abs" style="left:10px;top:34px;display:flex;gap:13px">
      <div style="width:40px"><div style="height:36px;background:linear-gradient(180deg,#f3f5f7,#d9e0e7)" role="img" aria-label="Team member portrait"></div><div style="font-size:2.8px;color:var(--blue);margin-top:2px">Name<br>Designation</div><p class="tiny">Lorem ipsum dolor sit amet, consectetur adipiscing elit, sed do eiusmod tempor incididunt ut labore.</p></div>
      <div style="width:40px"><div style="height:36px;background:linear-gradient(180deg,#f3f5f7,#d9e0e7)" role="img" aria-label="Team member portrait"></div><div style="font-size:2.8px;color:var(--blue);margin-top:2px">Name<br>Designation</div><p class="tiny">Lorem ipsum dolor sit amet, consectetur adipiscing elit, sed do eiusmod tempor incididunt ut labore.</p></div>
      <div style="width:40px"><div style="height:36px;background:linear-gradient(180deg,#f3f5f7,#d9e0e7)" role="img" aria-label="Team member portrait"></div><div style="font-size:2.8px;color:var(--blue);margin-top:2px">Name<br>Designation</div><p class="tiny">Lorem ipsum dolor sit amet, consectetur adipiscing elit, sed do eiusmod tempor incididunt ut labore.</p></div>
      <div style="width:40px"><div style="height:36px;background:linear-gradient(180deg,#f3f5f7,#d9e0e7)" role="img" aria-label="Team member portrait"></div><div style="font-size:2.8px;color:var(--blue);margin-top:2px">Name<br>Designation</div><p class="tiny">Lorem ipsum dolor sit amet, consectetur adipiscing elit, sed do eiusmod tempor incididunt ut labore.</p></div>
    </div>
    <div class="brand foot">Keystone Ridge</div><div class="pg">7</div>
  </section>

  <!-- 8 Our services -->
  <section class="slide c4 r2">
    <div class="abs photo-blue" style="left:0;top:0;width:228px;height:56px" role="img" aria-label="Blue toned photo of a city skyline"></div>
    <div class="title" style="color:#fff;top:18px">Our Services</div>
    <svg class="fill" viewBox="0 0 228 158" width="228" height="158">
      <circle cx="44" cy="56" r="8" fill="#45ade0" stroke="#fff" stroke-width="1.5"/>
      <circle cx="114" cy="56" r="8" fill="#45ade0" stroke="#fff" stroke-width="1.5"/>
      <circle cx="184" cy="56" r="8" fill="#8a9099" stroke="#fff" stroke-width="1.5"/>
    </svg>
    <div class="abs" style="left:10px;top:69px;width:208px;display:grid;grid-template-columns:repeat(3,1fr);gap:4px">
      <div><div style="font-size:3.2px;font-weight:700;color:var(--blue);text-align:center;margin-bottom:3px">INVESTING</div><ul class="list"><li>Managed Money</li><li>ETFs</li><li>Mutual Funds</li><li>Customized Portfolios</li><li>Private Placements</li></ul></div>
      <div><div style="font-size:3.2px;font-weight:700;color:var(--blue);text-align:center;margin-bottom:3px">FINANCIAL PLANNING</div><ul class="list"><li>Comprehensive Financial Planning</li><li>Detailed Financial Analysis</li><li>Tailored Financial Plans</li><li>Estate Planning Solutions</li><li>Planning for High Net Worth</li><li>Planning for High Income Earners</li></ul></div>
      <div><div style="font-size:3.2px;font-weight:700;color:var(--blue);text-align:center;margin-bottom:3px">INSURANCE</div><ul class="list"><li>General Liability</li><li>Auto</li><li>Home &amp; Umbrella</li><li>Life Insurance</li><li>Disability</li><li>Long-term Care</li></ul></div>
    </div>
    <div class="brand foot">Keystone Ridge</div><div class="pg">8</div>
  </section>

  <!-- 9 Photo with text -->
  <section class="slide c1 r3">
    <div class="title">Lorem ipsum dolor sit amet</div>
    <div class="abs" style="left:10px;top:37px;width:208px;height:105px;background:linear-gradient(100deg,#8fb7c9 0%,#d8e9c8 55%,#f4f1d6 100%)" role="img" aria-label="Photo of a family enjoying a sunny field"></div>
    <div class="abs" style="left:10px;top:37px;width:95px;height:105px;background:rgba(40,95,160,.75);padding:4px 4px">
      <ul class="list"><li style="color:#fff">Lorem ipsum dolor sit amet, consectetur adipiscing elit.</li><li style="color:#fff">Nam sit amet dictum neque, pretium fringilla metus. Nam bibendum urna in pharetra vehicula.</li><li style="color:#fff">Aenean luctus leo vitae quam elementum, ut semper libero faucibus. Maecenas eu magna sodales, finibus nisl vitae, finibus felis.</li></ul>
    </div>
    <div class="brand foot">Keystone Ridge</div><div class="pg">9</div>
  </section>

  <!-- 10 Map -->
  <section class="slide c2 r3">
    <div class="title">Lorem ipsum dolor sit amet</div>
    <div class="abs" style="left:10px;top:36px;width:155px;height:100px;background:linear-gradient(180deg,#eef0f2,#e4e7ea)" role="img" aria-label="World map with the United States highlighted in blue"></div>
    <p class="abs tiny" style="left:175px;top:38px;width:42px">Lorem ipsum dolor sit amet, consectetur adipiscing elit, sed do eiusmod tempor incididunt ut labore et dolore magna aliqua. Ut enim ad minim veniam, quis nostrud exercitation ullamco laboris nisi ut aliquip ex ea commodo consequat.</p>
    <div class="brand foot">Keystone Ridge</div><div class="pg">10</div>
  </section>

  <!-- 11 Labelled rows -->
  <section class="slide c3 r3">
    <div class="title">Lorem ipsum dolor sit amet</div>
    <div class="abs" style="left:10px;top:37px;width:208px;display:flex;flex-direction:column;gap:3px">
      <div style="display:flex;height:23px"><div style="width:32px;background:var(--steel-dark);color:#fff;font-size:3px;font-weight:700;padding:3px">Text 1</div><div style="flex:1;border:.6px solid var(--blue);padding:2px 4px"><ul class="list"><li>Lorem ipsum dolor sit amet, consectetur adipiscing elit, sed do eiusmod tempor incididunt ut labore et dolore magna aliqua. Ut enim ad minim veniam, quis nostrud exercitation ullamco laboris.</li></ul></div></div>
      <div style="display:flex;height:23px"><div style="width:32px;background:var(--steel-dark);color:#fff;font-size:3px;font-weight:700;padding:3px">Text 2</div><div style="flex:1;border:.6px solid var(--blue);padding:2px 4px"><ul class="list"><li>Lorem ipsum dolor sit amet, consectetur adipiscing elit, sed do eiusmod tempor incididunt ut labore et dolore magna aliqua. Ut enim ad minim veniam, quis nostrud exercitation ullamco laboris.</li></ul></div></div>
      <div style="display:flex;height:23px"><div style="width:32px;background:var(--steel-dark);color:#fff;font-size:3px;font-weight:700;padding:3px">Text 3</div><div style="flex:1;border:.6px solid var(--blue);padding:2px 4px"><ul class="list"><li>Lorem ipsum dolor sit amet, consectetur adipiscing elit, sed do eiusmod tempor incididunt ut labore et dolore magna aliqua. Ut enim ad minim veniam, quis nostrud exercitation ullamco laboris.</li></ul></div></div>
      <div style="display:flex;height:23px"><div style="width:32px;background:var(--blue);color:#fff;font-size:3px;font-weight:700;padding:3px">Text 4</div><div style="flex:1;border:.6px solid var(--blue);padding:2px 4px"><ul class="list"><li>Lorem ipsum dolor sit amet, consectetur adipiscing elit, sed do eiusmod tempor incididunt ut labore et dolore magna aliqua. Ut enim ad minim veniam, quis nostrud exercitation ullamco laboris.</li></ul></div></div>
    </div>
    <div class="brand foot">Keystone Ridge</div><div class="pg">11</div>
  </section>

  <!-- 12 Process band -->
  <section class="slide c4 r3">
    <div class="title">Lorem ipsum dolor sit amet</div>
    <div class="abs" style="left:10px;top:37px;width:208px;height:10px;background:var(--blue);display:grid;grid-template-columns:repeat(4,1fr);align-items:center;color:#fff;font-size:3.2px;text-align:center">
      <span>Item 1</span><span>Item 1</span><span>Item 1</span><span>Item 1</span>
    </div>
    <svg class="fill" viewBox="0 0 228 158" width="228" height="158">
      <g fill="#1f3b6f"><circle cx="62" cy="42" r="3"/><circle cx="114" cy="42" r="3"/><circle cx="166" cy="42" r="3"/></g>
      <g stroke="#fff" stroke-width=".7" fill="none"><path d="M61 40.5L63 42L61 43.5"/><path d="M113 40.5L115 42L113 43.5"/><path d="M165 40.5L167 42L165 43.5"/></g>
    </svg>
    <div class="abs" style="left:10px;top:51px;width:208px;display:grid;grid-template-columns:repeat(4,1fr);gap:8px">
      <ul class="list"><li>Lorem ipsum dolor sit amet, consectetur adipiscing elit, sed do eiusmod tempor incididunt ut labore et dolore magna aliqua. Ut enim ad minim veniam, quis nostrud exercitation ullamco laboris nisi.</li></ul>
      <ul class="list"><li>Lorem ipsum dolor sit amet, consectetur adipiscing elit, sed do eiusmod tempor incididunt ut labore et dolore magna aliqua. Ut enim ad minim veniam, quis nostrud exercitation ullamco laboris nisi.</li></ul>
      <ul class="list"><li>Lorem ipsum dolor sit amet, consectetur adipiscing elit, sed do eiusmod tempor incididunt ut labore et dolore magna aliqua. Ut enim ad minim veniam, quis nostrud exercitation ullamco laboris nisi.</li></ul>
      <ul class="list"><li>Lorem ipsum dolor sit amet, consectetur adipiscing elit, sed do eiusmod tempor incididunt ut labore et dolore magna aliqua. Ut enim ad minim veniam, quis nostrud exercitation ullamco laboris nisi.</li></ul>
    </div>
    <div class="brand foot">Keystone Ridge</div><div class="pg">12</div>
  </section>

  <!-- 13 Timeline cont'd -->
  <section class="slide c1 r4">
    <div class="title">Timeline (cont'd)</div>
    <svg class="fill" viewBox="0 0 228 158" width="228" height="158" font-family="Mulish,sans-serif">
      <line x1="10" y1="79" x2="218" y2="79" stroke="#9aa3ad" stroke-width=".5"/>
      <path d="M19 76L17 82M21 76L19 82" stroke="#9aa3ad" stroke-width=".5"/>
      <g stroke="#9aa3ad" stroke-width=".4"><line x1="22" y1="51" x2="22" y2="79"/><line x1="73" y1="51" x2="73" y2="79"/><line x1="124" y1="51" x2="124" y2="79"/><line x1="175" y1="51" x2="175" y2="79"/><line x1="47" y1="79" x2="47" y2="110"/><line x1="98" y1="79" x2="98" y2="110"/><line x1="149" y1="79" x2="149" y2="110"/></g>
      <g fill="#45ade0"><circle cx="22" cy="45" r="6"/><circle cx="73" cy="45" r="6"/><circle cx="124" cy="45" r="6"/><circle cx="175" cy="45" r="6"/><circle cx="47" cy="116" r="6"/><circle cx="98" cy="116" r="6"/><circle cx="149" cy="116" r="6"/></g>
      <g fill="#fff" stroke="#fff" stroke-width=".3"><circle cx="22" cy="79" r="1.2"/><circle cx="73" cy="79" r="1.2"/><circle cx="124" cy="79" r="1.2"/><circle cx="175" cy="79" r="1.2"/><circle cx="47" cy="79" r="1.2"/><circle cx="98" cy="79" r="1.2"/><circle cx="149" cy="79" r="1.2"/></g>
      <g fill="none" stroke="#45ade0" stroke-width=".6"><circle cx="22" cy="79" r="1.2"/><circle cx="73" cy="79" r="1.2"/><circle cx="124" cy="79" r="1.2"/><circle cx="175" cy="79" r="1.2"/><circle cx="47" cy="79" r="1.2"/><circle cx="98" cy="79" r="1.2"/><circle cx="149" cy="79" r="1.2"/></g>
      <g fill="#fff" font-size="3" text-anchor="middle"><text x="22" y="46">Year</text><text x="73" y="46">Year</text><text x="124" y="46">Year</text><text x="175" y="46">Year</text><text x="47" y="117">Year</text><text x="98" y="117">Year</text><text x="149" y="117">Year</text></g>
      <g fill="#5c6470" font-size="2.6"><text x="25" y="59">Lorem ipsum dolor sit</text><text x="25" y="63">amet, consectetur</text><text x="76" y="59">Lorem ipsum dolor sit</text><text x="76" y="63">amet, consectetur</text><text x="127" y="59">Lorem ipsum dolor sit</text><text x="127" y="63">amet, consectetur</text><text x="178" y="45">Lorem ipsum dolor sit</text><text x="178" y="49">amet, consectetur</text><text x="50" y="94">Lorem ipsum dolor sit</text><text x="50" y="98">amet, consectetur</text><text x="101" y="94">Lorem ipsum dolor sit</text><text x="101" y="98">amet, consectetur</text><text x="152" y="94">Lorem ipsum dolor sit</text><text x="152" y="98">amet, consectetur</text></g>
    </svg>
    <div class="brand foot">Keystone Ridge</div><div class="pg">13</div>
  </section>

  <!-- 14 Timeline -->
  <section class="slide c2 r4">
    <div class="title">Timeline</div>
    <svg class="fill" viewBox="0 0 228 158" width="228" height="158" font-family="Mulish,sans-serif">
      <line x1="10" y1="79" x2="218" y2="79" stroke="#9aa3ad" stroke-width=".5"/>
      <path d="M189 76L187 82M191 76L189 82" stroke="#9aa3ad" stroke-width=".5"/>
      <line x1="10" y1="76" x2="10" y2="82" stroke="#9aa3ad" stroke-width=".5"/>
      <g stroke="#9aa3ad" stroke-width=".4"><line x1="22" y1="51" x2="22" y2="79"/><line x1="73" y1="51" x2="73" y2="79"/><line x1="124" y1="51" x2="124" y2="79"/><line x1="175" y1="51" x2="175" y2="79"/><line x1="47" y1="79" x2="47" y2="110"/><line x1="98" y1="79" x2="98" y2="110"/><line x1="149" y1="79" x2="149" y2="110"/></g>
      <g fill="#45ade0"><circle cx="22" cy="45" r="6"/><circle cx="73" cy="45" r="6"/><circle cx="124" cy="45" r="6"/><circle cx="175" cy="45" r="6"/><circle cx="47" cy="116" r="6"/><circle cx="98" cy="116" r="6"/><circle cx="149" cy="116" r="6"/></g>
      <g fill="#fff" stroke="#45ade0" stroke-width=".6"><circle cx="22" cy="79" r="1.2"/><circle cx="73" cy="79" r="1.2"/><circle cx="124" cy="79" r="1.2"/><circle cx="175" cy="79" r="1.2"/><circle cx="47" cy="79" r="1.2"/><circle cx="98" cy="79" r="1.2"/><circle cx="149" cy="79" r="1.2"/></g>
      <g fill="#fff" font-size="3" text-anchor="middle"><text x="22" y="46">Year</text><text x="73" y="46">Year</text><text x="124" y="46">Year</text><text x="175" y="46">Year</text><text x="47" y="117">Year</text><text x="98" y="117">Year</text><text x="149" y="117">Year</text></g>
      <g fill="#5c6470" font-size="2.6"><text x="25" y="59">Lorem ipsum dolor sit</text><text x="25" y="63">amet, consectetur</text><text x="76" y="59">Lorem ipsum dolor sit</text><text x="76" y="63">amet, consectetur</text><text x="127" y="59">Lorem ipsum dolor sit</text><text x="127" y="63">amet, consectetur</text><text x="178" y="45">Lorem ipsum dolor sit</text><text x="178" y="49">amet, consectetur</text><text x="50" y="94">Lorem ipsum dolor sit</text><text x="50" y="98">amet, consectetur</text><text x="101" y="94">Lorem ipsum dolor sit</text><text x="101" y="98">amet, consectetur</text><text x="152" y="94">Lorem ipsum dolor sit</text><text x="152" y="98">amet, consectetur</text></g>
    </svg>
    <div class="brand foot">Keystone Ridge</div><div class="pg">14</div>
  </section>

  <!-- 15 Pros and cons -->
  <section class="slide c3 r4">
    <div class="title">Lorem ipsum dolor sit amet</div>
    <div class="abs" style="left:13px;top:33px;width:94px;height:20px;background:var(--blue);color:#fff;text-align:center;padding-top:4px">
      <svg width="7" height="7" viewBox="0 0 10 10"><path d="M2 9V4H4L6 1Q7.5 1 7 4H9V8L7.5 9Z" fill="none" stroke="#fff" stroke-width=".8"/></svg>
      <div style="font-size:3px;font-weight:700">PROS</div>
    </div>
    <div class="abs" style="left:120px;top:33px;width:94px;height:20px;background:var(--steel-dark);color:#fff;text-align:center;padding-top:4px">
      <svg width="7" height="7" viewBox="0 0 10 10"><path d="M2 1V6H4L6 9Q7.5 9 7 6H9V2L7.5 1Z" fill="none" stroke="#fff" stroke-width=".8"/></svg>
      <div style="font-size:3px;font-weight:700">CONS</div>
    </div>
    <div class="abs" style="left:13px;top:53px;width:94px;height:86px;border:.6px solid var(--blue);padding:5px 4px">
      <p class="tiny">✔ Lorem ipsum dolor sit amet</p><p class="tiny">✔ Consectetur adipiscing elit</p><p class="tiny">✔ Sed do eiusmod tempor incididunt ut labore et dolore magna aliqua</p><p class="tiny">✔ Consectetur adipiscing elit</p><p class="tiny">✔ Sed do eiusmod tempor incididunt ut labore et dolore magna aliqua</p>
    </div>
    <div class="abs" style="left:120px;top:53px;width:94px;height:86px;border:.6px solid var(--steel-dark);padding:5px 4px">
      <p class="tiny">✘ Lorem ipsum dolor sit amet</p><p class="tiny">✘ Consectetur adipiscing elit</p><p class="tiny">✘ Sed do eiusmod tempor incididunt ut labore et dolore magna aliqua</p><p class="tiny">✘ Consectetur adipiscing elit</p><p class="tiny">✘ Sed do eiusmod tempor incididunt ut labore et dolore magna aliqua</p>
    </div>
    <div class="brand foot">Keystone Ridge</div><div class="pg">15</div>
  </section>

  <!-- 16 Hub diagram -->
  <section class="slide c4 r4">
    <div class="title">Lorem ipsum dolor sit amet</div>
    <svg class="fill" viewBox="0 0 228 158" width="228" height="158" font-family="Mulish,sans-serif">
      <circle cx="114" cy="88" r="27" fill="none" stroke="#d5dbe2" stroke-width=".6"/>
      <circle cx="114" cy="88" r="20" fill="#8a9099"/>
      <g fill="#fff" font-size="3.4" text-anchor="middle"><text x="114" y="84">Lorem</text><text x="114" y="89">ipsum dolor</text><text x="114" y="94">sit amet</text></g>
      <g fill="#45ade0" stroke="#fff" stroke-width=".8">
        <circle cx="114" cy="55" r="6.5"/><circle cx="137" cy="65" r="6.5"/><circle cx="147" cy="88" r="6.5"/><circle cx="137" cy="111" r="6.5"/>
        <circle cx="114" cy="121" r="6.5"/><circle cx="91" cy="111" r="6.5"/><circle cx="81" cy="88" r="6.5"/><circle cx="91" cy="65" r="6.5"/>
      </g>
      <g fill="none" stroke="#fff" stroke-width=".6">
        <rect x="111" y="52" width="6" height="6"/><rect x="134" y="62" width="6" height="6"/><rect x="144" y="85" width="6" height="6"/><rect x="134" y="108" width="6" height="6"/>
        <rect x="111" y="118" width="6" height="6"/><rect x="88" y="108" width="6" height="6"/><rect x="78" y="85" width="6" height="6"/><rect x="88" y="62" width="6" height="6"/>
      </g>
      <g fill="#5c6470" font-size="2.6" text-anchor="middle">
        <text x="114" y="43">Lorem ipsum dolor sit amet,</text><text x="114" y="46.5">consectetur adipiscing elit</text>
        <text x="168" y="64">Lorem ipsum dolor sit amet,</text><text x="168" y="67.5">consectetur adipiscing elit</text>
        <text x="176" y="87">Lorem ipsum dolor sit amet,</text><text x="176" y="90.5">consectetur adipiscing elit</text>
        <text x="168" y="112">Lorem ipsum dolor sit amet,</text><text x="168" y="115.5">consectetur adipiscing elit</text>
        <text x="114" y="134">Lorem ipsum dolor sit amet,</text><text x="114" y="137.5">consectetur adipiscing elit</text>
        <text x="58" y="112">Lorem ipsum dolor sit amet,</text><text x="58" y="115.5">consectetur adipiscing elit</text>
        <text x="50" y="87">Lorem ipsum dolor sit amet,</text><text x="50" y="90.5">consectetur adipiscing elit</text>
        <text x="58" y="64">Lorem ipsum dolor sit amet,</text><text x="58" y="67.5">consectetur adipiscing elit</text>
      </g>
    </svg>
    <div class="brand foot">Keystone Ridge</div><div class="pg">16</div>
  </section>

  <!-- 17 Icon grid panel -->
  <section class="slide c1 r5">
    <div class="title">Lorem ipsum dolor sit amet</div>
    <svg class="abs" style="left:0;top:37px" width="228" height="106" viewBox="0 0 228 106" font-family="Mulish,sans-serif">
      <rect width="228" height="106" fill="#7aa3cb"/>
      <g stroke="#fff" stroke-width=".5" opacity=".7"><line x1="114" y1="0" x2="114" y2="53"/><line x1="0" y1="53" x2="228" y2="53"/><line x1="76" y1="53" x2="76" y2="106"/><line x1="152" y1="53" x2="152" y2="106"/></g>
      <g fill="#fff" font-size="3" text-anchor="middle"><text x="57" y="13">Lorem ipsum dolor sit amet</text><text x="171" y="12">Lorem ipsum dolor sit amet</text><text x="38" y="64">Lorem ipsum dolor sit amet</text><text x="114" y="64">Lorem ipsum dolor sit</text><text x="114" y="68">amet</text><text x="190" y="64">Lorem ipsum dolor sit amet</text></g>
      <g fill="none" stroke="#fff" stroke-width=".7">
        <path d="M50 34V24M54 34V28M58 34V20M62 34V26M48 34H66"/>
        <rect x="164" y="22" width="12" height="12"/><path d="M166 26H174M166 29H174"/>
        <circle cx="38" cy="85" r="5"/><path d="M38 82V88"/>
        <rect x="108" y="80" width="12" height="8"/><path d="M112 80V77H116V80"/>
        <path d="M184 86Q190 76 196 86Z"/><path d="M190 86V92"/>
      </g>
    </svg>
    <div class="brand foot">Keystone Ridge</div><div class="pg">17</div>
  </section>

  <!-- 18 Charts with text -->
  <section class="slide c2 r5">
    <div class="title">Lorem ipsum dolor sit amet</div>
    <div class="hdr" style="left:10px;top:39px;width:100px">Column Chart</div>
    <svg class="abs" style="left:10px;top:45px" width="100" height="44"><use href="#col-chart" width="100" height="44"/></svg>
    <div class="hdr" style="left:10px;top:91px;width:100px">Line Chart</div>
    <svg class="abs" style="left:10px;top:97px" width="100" height="44"><use href="#line-chart" width="100" height="44"/></svg>
    <div class="abs" style="left:118px;top:38px;width:100px">
      <ul class="list"><li>Lorem ipsum dolor sit amet, consectetur adipiscing elit, sed do eiusmod tempor incididunt ut labore et dolore magna aliqua. Ut enim ad minim veniam, quis nostrud exercitation.</li><li>Lorem ipsum dolor sit amet, consectetur adipiscing elit, sed do eiusmod tempor incididunt ut labore et dolore magna aliqua. Ut enim ad minim veniam, quis nostrud exercitation.</li><li>Lorem ipsum dolor sit amet, consectetur adipiscing elit, sed do eiusmod tempor incididunt ut labore et dolore magna aliqua. Ut enim ad minim veniam, quis nostrud exercitation.</li><li>Lorem ipsum dolor sit amet, consectetur adipiscing elit, sed do eiusmod tempor incididunt ut labore et dolore magna aliqua. Ut enim ad minim veniam, quis nostrud exercitation.</li></ul>
    </div>
    <div class="brand foot">Keystone Ridge</div><div class="pg">18</div>
  </section>

  <!-- 19 Comparison table, ratings -->
  <section class="slide c3 r5">
    <div class="title">Lorem ipsum dolor sit amet</div>
    <svg class="fill" viewBox="0 0 228 158" width="228" height="158" font-family="Mulish,sans-serif">
      <rect x="43" y="38" width="164" height="7" fill="#45ade0"/>
      <g fill="#fff" font-size="3" text-anchor="middle" font-weight="700"><text x="63.5" y="42.5">Factor 1</text><text x="104.5" y="42.5">Factor 2</text><text x="145.5" y="42.5">Factor 3</text><text x="186.5" y="42.5">Factor 4</text></g>
      <rect x="10" y="46" width="33" height="94" fill="#9aa3ad"/>
      <rect x="43" y="46" width="164" height="94" fill="#eceff2"/>
      <g stroke="#fff" stroke-width=".5"><line x1="10" y1="56.5" x2="207" y2="56.5"/><line x1="10" y1="67" x2="207" y2="67"/><line x1="10" y1="77.5" x2="207" y2="77.5"/><line x1="10" y1="88" x2="207" y2="88"/><line x1="10" y1="98.5" x2="207" y2="98.5"/><line x1="10" y1="109" x2="207" y2="109"/><line x1="10" y1="119.5" x2="207" y2="119.5"/><line x1="10" y1="130" x2="207" y2="130"/></g>
      <g fill="#fff" font-size="3" font-weight="700"><text x="12" y="52.5">Product 1</text><text x="12" y="63">Product 2</text><text x="12" y="73.5">Product 3</text><text x="12" y="84">Product 4</text><text x="12" y="94.5">Product 5</text><text x="12" y="105">Product 6</text><text x="12" y="115.5">Product 7</text><text x="12" y="126">Product 8</text><text x="12" y="136.5">Product 9</text></g>
      <g>
        <use href="#hb3" x="60.5" y="48" width="6" height="6"/><use href="#hb1" x="101.5" y="48" width="6" height="6"/><use href="#hb4" x="142.5" y="48" width="6" height="6"/><use href="#hb2" x="183.5" y="48" width="6" height="6"/>
        <use href="#hb0" x="60.5" y="58.5" width="6" height="6"/><use href="#hb0" x="101.5" y="58.5" width="6" height="6"/><use href="#hb2" x="142.5" y="58.5" width="6" height="6"/><use href="#hb0" x="183.5" y="58.5" width="6" height="6"/>
        <use href="#hb3" x="60.5" y="69" width="6" height="6"/><use href="#hb2" x="101.5" y="69" width="6" height="6"/><use href="#hb0" x="142.5" y="69" width="6" height="6"/><use href="#hb3" x="183.5" y="69" width="6" height="6"/>
        <use href="#hb3" x="60.5" y="79.5" width="6" height="6"/><use href="#hb2" x="101.5" y="79.5" width="6" height="6"/><use href="#hb1" x="142.5" y="79.5" width="6" height="6"/><use href="#hb1" x="183.5" y="79.5" width="6" height="6"/>
        <use href="#hb2" x="60.5" y="90" width="6" height="6"/><use href="#hb2" x="101.5" y="90" width="6" height="6"/><use href="#hb2" x="142.5" y="90" width="6" height="6"/><use href="#hb3" x="183.5" y="90" width="6" height="6"/>
        <use href="#hb2" x="60.5" y="100.5" width="6" height="6"/><use href="#hb4" x="101.5" y="100.5" width="6" height="6"/><use href="#hb2" x="142.5" y="100.5" width="6" height="6"/><use href="#hb4" x="183.5" y="100.5" width="6" height="6"/>
        <use href="#hb2" x="60.5" y="111" width="6" height="6"/><use href="#hb2" x="101.5" y="111" width="6" height="6"/><use href="#hb4" x="142.5" y="111" width="6" height="6"/><use href="#hb2" x="183.5" y="111" width="6" height="6"/>
        <use href="#hb2" x="60.5" y="121.5" width="6" height="6"/><use href="#hb4" x="101.5" y="121.5" width="6" height="6"/><use href="#hb0" x="142.5" y="121.5" width="6" height="6"/><use href="#hb3" x="183.5" y="121.5" width="6" height="6"/>
        <use href="#hb0" x="60.5" y="132" width="6" height="6"/><use href="#hb2" x="101.5" y="132" width="6" height="6"/><use href="#hb1" x="142.5" y="132" width="6" height="6"/><use href="#hb0" x="183.5" y="132" width="6" height="6"/>
      </g>
    </svg>
    <div class="brand foot">Keystone Ridge</div><div class="pg">19</div>
  </section>

  <!-- 20 Comparison table, ticks -->
  <section class="slide c4 r5">
    <div class="title">Lorem ipsum dolor sit amet</div>
    <svg class="fill" viewBox="0 0 228 158" width="228" height="158" font-family="Mulish,sans-serif">
      <rect x="43" y="38" width="164" height="7" fill="#45ade0"/>
      <g fill="#fff" font-size="3" text-anchor="middle" font-weight="700"><text x="63.5" y="42.5">Factor 1</text><text x="104.5" y="42.5">Factor 2</text><text x="145.5" y="42.5">Factor 3</text><text x="186.5" y="42.5">Factor 4</text></g>
      <rect x="10" y="46" width="33" height="94" fill="#9aa3ad"/>
      <rect x="43" y="46" width="164" height="94" fill="#eceff2"/>
      <g stroke="#fff" stroke-width=".5"><line x1="10" y1="56.5" x2="207" y2="56.5"/><line x1="10" y1="67" x2="207" y2="67"/><line x1="10" y1="77.5" x2="207" y2="77.5"/><line x1="10" y1="88" x2="207" y2="88"/><line x1="10" y1="98.5" x2="207" y2="98.5"/><line x1="10" y1="109" x2="207" y2="109"/><line x1="10" y1="119.5" x2="207" y2="119.5"/><line x1="10" y1="130" x2="207" y2="130"/></g>
      <g fill="#fff" font-size="3" font-weight="700"><text x="12" y="52.5">Product 1</text><text x="12" y="63">Product 2</text><text x="12" y="73.5">Product 3</text><text x="12" y="84">Product 4</text><text x="12" y="94.5">Product 5</text><text x="12" y="105">Product 6</text><text x="12" y="115.5">Product 7</text><text x="12" y="126">Product 8</text><text x="12" y="136.5">Product 9</text></g>
      <g>
        <use href="#tick" x="60.5" y="48" width="6" height="6"/><use href="#tick" x="101.5" y="48" width="6" height="6"/><use href="#tick" x="142.5" y="48" width="6" height="6"/><use href="#tick" x="183.5" y="48" width="6" height="6"/>
        <use href="#tick" x="60.5" y="58.5" width="6" height="6"/><use href="#tick" x="101.5" y="58.5" width="6" height="6"/><use href="#cross" x="142.5" y="58.5" width="6" height="6"/><use href="#tick" x="183.5" y="58.5" width="6" height="6"/>
        <use href="#tick" x="60.5" y="69" width="6" height="6"/><use href="#tick" x="101.5" y="69" width="6" height="6"/><use href="#tick" x="142.5" y="69" width="6" height="6"/><use href="#cross" x="183.5" y="69" width="6" height="6"/>
        <use href="#tick" x="60.5" y="79.5" width="6" height="6"/><use href="#cross" x="101.5" y="79.5" width="6" height="6"/><use href="#tick" x="142.5" y="79.5" width="6" height="6"/><use href="#tick" x="183.5" y="79.5" width="6" height="6"/>
        <use href="#tick" x="60.5" y="90" width="6" height="6"/><use href="#tick" x="101.5" y="90" width="6" height="6"/><use href="#tick" x="142.5" y="90" width="6" height="6"/><use href="#tick" x="183.5" y="90" width="6" height="6"/>
        <use href="#tick" x="60.5" y="100.5" width="6" height="6"/><use href="#cross" x="101.5" y="100.5" width="6" height="6"/><use href="#tick" x="142.5" y="100.5" width="6" height="6"/><use href="#tick" x="183.5" y="100.5" width="6" height="6"/>
        <use href="#tick" x="60.5" y="111" width="6" height="6"/><use href="#tick" x="101.5" y="111" width="6" height="6"/><use href="#tick" x="142.5" y="111" width="6" height="6"/><use href="#tick" x="183.5" y="111" width="6" height="6"/>
        <use href="#tick" x="60.5" y="121.5" width="6" height="6"/><use href="#tick" x="101.5" y="121.5" width="6" height="6"/><use href="#cross" x="142.5" y="121.5" width="6" height="6"/><use href="#tick" x="183.5" y="121.5" width="6" height="6"/>
        <use href="#tick" x="60.5" y="132" width="6" height="6"/><use href="#tick" x="101.5" y="132" width="6" height="6"/><use href="#tick" x="142.5" y="132" width="6" height="6"/><use href="#tick" x="183.5" y="132" width="6" height="6"/>
      </g>
    </svg>
    <div class="brand foot">Keystone Ridge</div><div class="pg">20</div>
  </section>

  <!-- 21 Two charts with notes -->
  <section class="slide c1 r6">
    <div class="title">Lorem ipsum dolor sit amet</div>
    <div class="hdr" style="left:10px;top:37px;width:100px">Column Chart</div>
    <svg class="abs" style="left:10px;top:43px" width="100" height="44"><use href="#col-chart" width="100" height="44"/></svg>
    <div class="hdr" style="left:118px;top:37px;width:100px">Line Chart</div>
    <svg class="abs" style="left:118px;top:43px" width="100" height="44"><use href="#line-chart" width="100" height="44"/></svg>
    <ul class="list abs" style="left:10px;top:92px;width:100px"><li>Lorem ipsum dolor sit amet, consectetur adipiscing elit, sed do eiusmod tempor incididunt ut labore et dolore magna aliqua.</li><li>Lorem ipsum dolor sit amet, consectetur adipiscing elit, sed do eiusmod tempor incididunt ut labore et dolore magna aliqua.</li></ul>
    <ul class="list abs" style="left:118px;top:92px;width:100px"><li>Lorem ipsum dolor sit amet, consectetur adipiscing elit, sed do eiusmod tempor incididunt ut labore et dolore magna aliqua.</li><li>Lorem ipsum dolor sit amet, consectetur adipiscing elit, sed do eiusmod tempor incididunt ut labore et dolore magna aliqua.</li></ul>
    <div class="brand foot">Keystone Ridge</div><div class="pg">21</div>
  </section>

  <!-- 22 Charts, table and pie -->
  <section class="slide c2 r6">
    <div class="title">Lorem ipsum dolor sit amet</div>
    <div class="hdr" style="left:10px;top:37px;width:100px">Column Chart</div>
    <svg class="abs" style="left:10px;top:43px" width="100" height="44"><use href="#col-chart" width="100" height="44"/></svg>
    <div class="hdr" style="left:118px;top:37px;width:100px">Line Chart</div>
    <svg class="abs" style="left:118px;top:43px" width="100" height="44"><use href="#line-chart" width="100" height="44"/></svg>
    <div class="hdr" style="left:10px;top:90px;width:100px">Table</div>
    <svg class="abs" style="left:10px;top:96px" width="100" height="46" viewBox="0 0 100 46" font-family="Mulish,sans-serif">
      <g fill="#45ade0" font-size="2.6" text-anchor="middle"><text x="16" y="4">Item 1</text><text x="50" y="4">Item 2</text><text x="84" y="4">Item 3</text></g>
      <g fill="#eceff2"><rect y="6" width="100" height="7"/><rect y="20" width="100" height="7"/><rect y="34" width="100" height="7"/></g>
      <g fill="#5c6470" font-size="2.6" text-anchor="middle">
        <text x="16" y="11">1.0</text><text x="50" y="11">1.0</text><text x="84" y="11">1.0</text>
        <text x="16" y="18">2.0</text><text x="50" y="18">2.0</text><text x="84" y="18">2.0</text>
        <text x="16" y="25">3.0</text><text x="50" y="25">3.0</text><text x="84" y="25">3.0</text>
        <text x="16" y="32">4.0</text><text x="50" y="32">4.0</text><text x="84" y="32">4.0</text>
        <text x="16" y="39">5.0</text><text x="50" y="39">5.0</text><text x="84" y="39">5.0</text>
      </g>
    </svg>
    <div class="hdr" style="left:118px;top:90px;width:100px">Pie Chart</div>
    <svg class="abs" style="left:118px;top:96px" width="100" height="46" viewBox="0 0 100 46" font-family="Mulish,sans-serif">
      <circle cx="42" cy="22" r="9" fill="none" stroke="#1f3b6f" stroke-width="4" stroke-dasharray="36 100" transform="rotate(-90 42 22)"/>
      <circle cx="42" cy="22" r="9" fill="none" stroke="#45ade0" stroke-width="4" stroke-dasharray="0 36 12 100" transform="rotate(-90 42 22)"/>
      <circle cx="42" cy="22" r="9" fill="none" stroke="#a9c3da" stroke-width="4" stroke-dasharray="0 48 8.5 100" transform="rotate(-90 42 22)"/>
      <g fill="#5c6470" font-size="2.4"><text x="78" y="16">■ 1st Qtr</text><text x="78" y="20">■ 2nd Qtr</text><text x="78" y="24">■ 3rd Qtr</text><text x="78" y="28">■ 4th Qtr</text></g>
    </svg>
    <div class="brand foot">Keystone Ridge</div><div class="pg">22</div>
  </section>

  <!-- 23 Contact -->
  <section class="slide c3 r6">
    <div class="fill photo-blue" role="img" aria-label="Blue toned photo of a customer service agent with headset"></div>
    <div class="abs" style="left:20px;top:46px;color:#fff;font-size:14px;font-weight:300;line-height:1;letter-spacing:.5px">CONTACT<br>US</div>
    <div class="brand white" style="left:30px;top:82px">Keystone Ridge</div>
    <div class="abs tiny white" style="left:20px;top:112px;width:100px;font-size:2.6px">480 Harbor Way, Suite 210, Riverton, OR 97000<br>info@keystoneridge.example · +1 555 010 2048</div>
  </section>

  <!-- 24 Thank you -->
  <section class="slide c4 r6">
    <div class="fill photo-desk" style="background:linear-gradient(135deg,#f7f8fa,#e8ecf0 60%,#f4efe2)" role="img" aria-label="Photo of two business people shaking hands"></div>
    <div class="abs" style="left:0;top:114px;width:228px;height:44px;background:var(--blue-soft)"></div>
    <div class="abs" style="left:10px;top:118px;color:#fff;font-size:14px;font-weight:300;line-height:1;letter-spacing:.5px">THANK<br>YOU</div>
    <div class="brand white" style="right:12px;top:124px">Keystone Ridge</div>
    <div class="abs tiny white" style="right:10px;top:144px;font-size:2.4px">keystoneridge.example · 480 Harbor Way, Riverton · +1 555 010 2048</div>
  </section>

</main>
</body>
</html>
```